Powder Bag Design for supplement company

We need a new bag design for our marine phytoplankton supplement.
we currently have a foil bag with a sticker and we want a full colored design. we are 100% vegan and sustainable. We would want to stick on brand which is a deep blue/purple. (img for reference.) We want a modern updated feel to compete in the market. Playing off of the ocean would be a bonus

Target Market(s)

ages 35+

Industry/Entity Type

health and wellness

```html
<!DOCTYPE html>
<html lang="en">
<head>
<meta charset="UTF-8">
<title>Nerida – Marine Phytoplankton Pouch</title>
<link rel="stylesheet" href="https://fonts.googleapis.com/css2?family=Poppins:wght@400;500&family=Libre+Baskerville:wght@700&display=swap">
<style>
  :root {
    --backdrop: #e6e3ef;
    --pouch-white: #f4f4f5;
    --ink-navy: #1b1538;
    --ocean-light: #a9cfd3;
    --ocean-mid: #4f8fa6;
    --ocean-deep: #1f5a7c;
    --ocean-dark: #1d4560;
    --label-white: #ffffff;
    --tag-grey: #e4e4e8;
    --seal-line: #dcdcdf;
  }
  * { margin: 0; padding: 0; box-sizing: border-box; }
  html, body { width: 1200px; height: 1000px; overflow: hidden; }
  body { background: var(--backdrop); position: relative; }

  .pouch {
    position: absolute;
    left: 345px; top: 125px;
    width: 510px; height: 740px;
    background: var(--pouch-white);
    overflow: hidden;
  }
  .pouch__seal {
    position: absolute; left: 0; right: 0; top: 82px;
    height: 6px;
    border-top: 1px solid var(--seal-line);
    border-bottom: 1px solid var(--seal-line);
  }
  .brand {
    position: absolute; left: 0; right: 0; top: 130px;
    text-align: center;
    font-family: "Poppins", sans-serif;
    font-weight: 500;
    font-size: 78px;
    line-height: 1;
    color: var(--ink-navy);
    letter-spacing: 1px;
  }
  .brand__mark {
    display: inline-block;
    width: 9px; height: 9px;
    border: 1.5px solid var(--ink-navy);
    border-radius: 50%;
    vertical-align: top;
    margin-left: 6px; margin-top: 14px;
  }
  .tagline {
    position: absolute; left: 0; right: 0; top: 240px;
    text-align: center;
    font-family: "Libre Baskerville", serif;
    font-weight: 700;
    font-size: 10.5px;
    letter-spacing: 0.2px;
    color: var(--ink-navy);
  }
  .ocean-wash {
    position: absolute; left: 0; right: 0; top: 330px; bottom: 0;
    background: linear-gradient(180deg,
      rgba(244,244,245,0) 0%,
      var(--ocean-light) 32%,
      var(--ocean-mid) 50%,
      var(--ocean-deep) 58%,
      var(--ocean-mid) 70%,
      var(--ocean-deep) 88%,
      var(--ocean-dark) 100%);
  }
  .claims {
    position: absolute; left: 103px; top: 596px;
    width: 322px; height: 46px;
    font-family: "Poppins", sans-serif;
    font-weight: 500;
    font-size: 13px;
    color: var(--label-white);
  }
  .claims__item { position: absolute; line-height: 20px; }
  .claims__item--tl { left: 0; top: 3px; }
  .claims__item--bl { left: 0; top: 28px; }
  .claims__item--tr { right: 0; top: 3px; }
  .claims__item--br { right: 0; top: 28px; }
  .claims__rule-h {
    position: absolute; left: 0; right: 0; top: 25px;
    height: 1.5px; background: var(--label-white);
  }
  .claims__rule-v {
    position: absolute; left: 171px; top: 5px;
    width: 1.5px; height: 41px; background: var(--label-white);
  }
  .net-weight {
    position: absolute; left: 230px; top: 692px;
    width: 73px; height: 48px;
    background: var(--tag-grey);
    font-family: "Poppins", sans-serif;
    font-size: 13px;
    color: var(--ink-navy);
    display: flex; align-items: center; justify-content: center;
  }
</style>
</head>
<body>
  <main class="pouch">
    <div class="pouch__seal"></div>
    <h1 class="brand">Nerida<span class="brand__mark"></span></h1>
    <p class="tagline">FOR GOOD HEALTH / POUR UNE BONNE SANTÉ</p>
    <div class="ocean-wash" role="img" aria-label="Blue watercolour ocean wash fading up from the bottom of the pouch"></div>
    <section class="claims">
      <span class="claims__item claims__item--tl">OMEGAB B3-6-7-9</span>
      <span class="claims__item claims__item--bl">VEGAN</span>
      <span class="claims__item claims__item--tr">ADAPTOGENS</span>
      <span class="claims__item claims__item--br">PROBIOTICS</span>
      <div class="claims__rule-h"></div>
      <div class="claims__rule-v"></div>
    </section>
    <div class="net-weight">100 GR</div>
  </main>
</body>
</html>
```